Plumbing distributor looking for flyer to advertise new product line

We are looking for a flyer to advertise a new product line we are carrying. We are plumbing wholesale distributor that sells to plumbing and fire sprinkler contractors. We are expanding our product line to sell fire pump repair parts (Link to Wiki on what a fire pump is https://en.corvapedia.org/wiki/Fire_pump)
We are wanting a flyer have the manufacturers logos we are carrying parts for as well as talking about our technical assistance and same day shipping.
The product types we will be carrying are
Fire Pump repack kits
Fast Packs
Case Gaskets
Packing
Gland Bolt Assemblies
Lantern Rings
Bearings
Jockey Pumps

If you want to find other images you can google any of the fire pump manufacture names with "fire pump" to find other images

Our website is www.quillvanesupply.com

Industry/Entity Type

Wholesale

Colors

Designer to choose colors to be used in the design.

Requirements
Must have
• Be targeted to businesses not retail

```html
<!DOCTYPE html>
<html lang="en">
<head>
<meta charset="utf-8">
<title>Quillvane Supply – Fire Pump Repair Parts Flyer</title>
<link href="https://fonts.googleapis.com/css2?family=Open+Sans:wght@400;600;700&display=swap" rel="stylesheet">
<style>
  :root {
    --blue: #3b4ea6;
    --blue-deep: #2f3f93;
    --blue-panel: #4357b3;
    --purple: #6a4bb0;
    --pink: #e8245a;
    --paper: #f2f2f4;
    --ink: #2b2b2b;
    --white: #ffffff;
  }
  * { box-sizing: border-box; margin: 0; padding: 0; }
  html, body { width: 850px; height: 1200px; overflow: hidden; background: var(--paper); }
  body { font-family: "Open Sans", Arial, sans-serif; color: var(--ink); }

  .flyer { position: relative; width: 850px; height: 1200px; background: var(--paper); overflow: hidden; }

  .hero { position: absolute; left: 0; top: 0; width: 850px; height: 520px; }

  .brand { position: absolute; left: 34px; top: 492px; display: flex; align-items: center; gap: 14px; }
  .brand__mark { width: 50px; height: 50px; background: var(--blue); }
  .brand__name { font-size: 31px; font-weight: 400; color: var(--blue); line-height: 1.05; }
  .brand__sub { font-size: 18px; color: var(--blue); line-height: 1.1; }

  .intro { position: absolute; left: 34px; top: 568px; width: 420px; font-size: 16.2px; line-height: 23px; color: var(--ink); }
  .intro p + p { margin-top: 8px; }

  .product-photo { position: absolute; left: 470px; top: 500px; width: 370px; height: 300px;
    background: radial-gradient(ellipse at 45% 60%, #d8232e 0%, #b81c25 40%, rgba(242,242,244,0) 72%); }

  .featured { position: absolute; left: 39px; top: 870px; width: 236px; height: 186px; border: 5px solid var(--blue); background: var(--white); }
  .featured__name { display: block; margin: 8px auto 0; width: 170px; text-align: center; font-size: 26px; font-weight: 700; color: var(--blue-deep); letter-spacing: 1px; }
  .featured__photo { position: absolute; left: 18px; right: 18px; top: 52px; bottom: 10px;
    background: linear-gradient(90deg, #8c8f96 0%, #b89b5a 50%, #9a7a3e 100%); border-radius: 4px; }

  .range { position: absolute; left: 885px; }
  .range { left: 888px; }
  .types { position: absolute; left: 888px; }

  .types-panel { position: absolute; left: 888px; }
  .catalogue { position: absolute; left: 888px; }

  .lineup { position: absolute; left: 888px; }

  .product-types { position: absolute; left: 888px; }

  .offer { position: absolute; left: 888px; top: 875px; }

  .product-list { position: absolute; left: 888px; }
  .parts { position: absolute; left: 338px; top: 875px; width: 512px; height: 188px; background: var(--blue-panel); border-radius: 22px 0 0 22px; overflow: hidden; }
  .parts__title { height: 46px; background: var(--blue-deep); color: var(--white); font-size: 21px; font-weight: 700; padding: 10px 0 0 32px; }
  .parts__cols { display: flex; padding: 18px 0 0 32px; gap: 22px; }
  .parts__col { list-style: none; }
  .parts__col:nth-child(1) { width: 150px; }
  .parts__col:nth-child(2) { width: 128px; }
  .parts__item { display: flex; align-items: flex-start; gap: 10px; color: var(--white); font-size: 15px; line-height: 18px; margin-bottom: 14px; }
  .parts__icon { flex: none; width: 12px; height: 12px; margin-top: 3px; }

  .makers { position: absolute; left: 30px; top: 1080px; width: 790px; display: flex; justify-content: space-between; align-items: center; }
  .makers__name { font-size: 17px; font-weight: 700; color: var(--blue-deep); }

  .contact { position: absolute; left: 0; top: 1147px; width: 850px; height: 53px; }
  .contact__call { position: absolute; left: 48px; top: 10px; font-size: 29px; font-weight: 700; color: var(--white); }
  .contact__call span { font-weight: 400; }
  .contact__web { position: absolute; right: 30px; top: 14px; font-size: 22px; font-weight: 700; color: var(--white); }
</style>
</head>
<body>
<main class="flyer">

  <svg class="hero" viewBox="0 0 850 520" aria-hidden="false">
    <defs>
      <linearGradient id="photoTone" x1="0" y1="0" x2="1" y2="1">
        <stop offset="0" stop-color="#c9cbd0"/>
        <stop offset="0.35" stop-color="#c3242b"/>
        <stop offset="0.65" stop-color="#d8333a"/>
        <stop offset="1" stop-color="#a9adb5"/>
      </linearGradient>
      <linearGradient id="wedgeLeft" x1="0" y1="0" x2="1" y2="0">
        <stop offset="0" stop-color="#6a4bb0"/>
        <stop offset="1" stop-color="#3b4ea6"/>
      </linearGradient>
    </defs>
    <rect x="0" y="0" width="850" height="420" fill="url(#photoTone)" role="img" aria-label="Photograph of a red fire pump installation with piping in a plant room"/>
    <polygon points="0,400 850,400 850,520 0,520" fill="#f2f2f4"/>
    <polygon points="0,395 470,380 850,468 850,520 0,520" fill="#f2f2f4"/>
    <polygon points="0,318 470,382 0,396" fill="url(#wedgeLeft)"/>
    <polygon points="0,396 470,382 850,468 850,516" fill="#e8245a"/>
    <polygon points="470,382 850,262 850,468" fill="#3b4ea6"/>
  </svg>

  <header class="brand">
    <div class="brand__mark"></div>
    <div>
      <div class="brand__name">Quillvane Supply</div>
      <div class="brand__sub">Company</div>
    </div>
  </header>

  <section class="intro">
    <p>Quillvane Supply Company is your complete source for backflow preventer repair parts, accessories and enclosures. Founded in 1976, our company is the nation’s leading backflow preventer specialist, trusted by thousands of technicians, plumbing contractors, fire line contractors, irrigation contractors, building managers and city officials across the country.</p>
    <p>Our dedication to providing the most comprehensive selection of backflow preventer repair parts is second to none and only matched by the knowledge of our highly trained staff.</p>
  </section>

  <div class="product-photo" role="img" aria-label="Photograph of a red split-case fire pump with a brass valve"></div>

  <figure class="featured">
    <span class="featured__name">HARLOW</span>
    <div class="featured__photo" role="img" aria-label="Photograph of brass and steel relief valves"></div>
  </figure>

  <section class="parts">
    <h2 class="parts__title">The product types we will be carrying are</h2>
    <div class="parts__cols">
      <ul class="parts__col">
        <li class="parts__item"><svg class="parts__icon" viewBox="0 0 12 12"><path d="M1 9 L6 3 L11 9" fill="none" stroke="#fff" stroke-width="2"/></svg>Fire Pump<br>repack kits</li>
        <li class="parts__item"><svg class="parts__icon" viewBox="0 0 12 12"><path d="M1 9 L6 3 L11 9" fill="none" stroke="#fff" stroke-width="2"/></svg>Fast Packs</li>
        <li class="parts__item"><svg class="parts__icon" viewBox="0 0 12 12"><path d="M1 9 L6 3 L11 9" fill="none" stroke="#fff" stroke-width="2"/></svg>Case Gaskets</li>
      </ul>
      <ul class="parts__col">
        <li class="parts__item"><svg class="parts__icon" viewBox="0 0 12 12"><path d="M1 9 L6 3 L11 9" fill="none" stroke="#fff" stroke-width="2"/></svg>Packing</li>
        <li class="parts__item"><svg class="parts__icon" viewBox="0 0 12 12"><path d="M1 9 L6 3 L11 9" fill="none" stroke="#fff" stroke-width="2"/></svg>Gland Bolt<br>Assemblies</li>
        <li class="parts__item"><svg class="parts__icon" viewBox="0 0 12 12"><path d="M1 9 L6 3 L11 9" fill="none" stroke="#fff" stroke-width="2"/></svg>Lantern Rings</li>
      </ul>
      <ul class="parts__col">
        <li class="parts__item"><svg class="parts__icon" viewBox="0 0 12 12"><path d="M1 9 L6 3 L11 9" fill="none" stroke="#fff" stroke-width="2"/></svg>Bearings</li>
        <li class="parts__item"><svg class="parts__icon" viewBox="0 0 12 12"><path d="M1 9 L6 3 L11 9" fill="none" stroke="#fff" stroke-width="2"/></svg>Jockey Pumps</li>
      </ul>
    </div>
  </section>

  <div class="makers">
    <span class="makers__name">Brinmoor</span>
    <span class="makers__name">Torvex</span>
    <span class="makers__name">Kessler</span>
    <span class="makers__name">Ashgrove Marsh</span>
    <span class="makers__name">Velden</span>
    <span class="makers__name">Stallard Pump</span>
  </div>

  <footer class="contact">
    <svg width="850" height="53" viewBox="0 0 850 53" style="position:absolute;left:0;top:0">
      <rect x="0" y="0" width="850" height="53" fill="#3b4ea6"/>
      <polygon points="488,0 498,0 482,53 472,53" fill="#ffffff"/>
    </svg>
    <div class="contact__call">Call now: <span>800.555.0142</span></div>
    <div class="contact__web">www.quillvanesupply.com</div>
  </footer>

</main>
</body>
</html>
```